Business Card Design Project

The business card should have the MBH logo. (see attachment)
The web address. Marshbirchhaven.net

Target Market(s)

Paragliding pilots.

Industry/Entity Type

Business

Requirements
Must have
• The logo and web address. 2 paragliding wings. The attached file provides the logo color scheme and font style.
Nice to have
• Paragliding pilots enjoy the outdoors so an outdoor background would be nice. The background should not be to detailed.

```html
<!DOCTYPE html>
<html lang="en">
<head>
<meta charset="utf-8">
<title>MBH Business Card</title>
<link href="https://fonts.googleapis.com/css2?family=Open+Sans:wght@400;700&display=swap" rel="stylesheet">
<style>
  :root {
    --page-bg: #e9e6e1;
    --card-black: #121315;
    --card-black-soft: #1c1d20;
    --placeholder-top: #2e2f32;
    --placeholder-bottom: #222326;
    --accent-yellow: #f6ee1a;
    --brand-blue: #0a5aa8;
    --text-white: #e8e8e8;
  }
  html, body {
    margin: 0;
    width: 1200px;
    height: 913px;
    overflow: hidden;
    background: var(--page-bg);
    font-family: "Open Sans", Arial, sans-serif;
  }
  .stage {
    position: relative;
    width: 1200px;
    height: 913px;
  }
  .card {
    position: absolute;
    top: 300px;
    width: 525px;
    height: 300px;
    background: linear-gradient(160deg, var(--card-black-soft), var(--card-black));
    border-radius: 4px;
    overflow: hidden;
    box-shadow: 0 14px 30px rgba(0,0,0,.25);
  }
  .card--front { left: 50px; }
  .card--back { left: 625px; }

  .illustration-area {
    position: absolute;
    background: linear-gradient(180deg, var(--placeholder-top), var(--placeholder-bottom));
    border-radius: 3px;
  }

  .brand-name {
    position: absolute;
    margin: 0;
    font-weight: 700;
    color: var(--brand-blue);
    letter-spacing: 2px;
    line-height: 1;
  }
  .card--front .brand-name { left: 165px; top: 110px; font-size: 76px; }
  .card--back .brand-name { left: 90px; top: 138px; font-size: 56px; }

  .person {
    position: absolute;
    right: 24px;
    top: 24px;
    text-align: right;
  }
  .person__name {
    margin: 0;
    font-size: 17px;
    font-weight: 700;
    color: var(--accent-yellow);
  }
  .person__role {
    margin: 0;
    font-size: 11px;
    color: var(--text-white);
  }
  .contacts {
    position: absolute;
    right: 24px;
    top: 120px;
    margin: 0;
    padding: 0;
    list-style: none;
    font-size: 12px;
    color: var(--text-white);
    text-align: right;
  }
  .contacts li {
    display: flex;
    justify-content: flex-end;
    align-items: center;
    gap: 8px;
    height: 20px;
  }
  .contacts svg { width: 12px; height: 12px; fill: var(--accent-yellow); }

  .edge-band {
    position: absolute;
    left: 0;
    bottom: 0;
    width: 100%;
    height: 14px;
  }
</style>
</head>
<body>
<main class="stage">

  <section class="card card--front" aria-label="Card front">
    <div class="illustration-area" style="left:380px; top:18px; width:125px; height:100px;" role="img" aria-label="Faint paraglider and pilot silhouette"></div>
    <div class="illustration-area" style="left:24px; top:200px; width:170px; height:80px;" role="img" aria-label="Faint paraglider and pilot silhouette"></div>
    <p class="brand-name">MBH</p>
  </section>

  <section class="card card--back" aria-label="Card back">
    <div class="illustration-area" style="left:160px; top:45px; width:180px; height:70px;" role="img" aria-label="Faint paraglider and pilot silhouette"></div>

    <div class="person">
      <p class="person__name">Your Long Name</p>
      <p class="person__role">Managing Director</p>
    </div>

    <ul class="contacts">
      <li>00359 555 0142 00
        <svg viewBox="0 0 12 12"><path d="M2 1h3l1 3-2 1a7 7 0 0 0 3 3l1-2 3 1v3c-6 0-9-3-9-9z"/></svg></li>
      <li>info@marshbirchhaven.net
        <svg viewBox="0 0 12 12"><path d="M0 2h12v8H0z"/></svg></li>
      <li>www.marshbirchhaven.net
        <svg viewBox="0 0 12 12"><circle cx="6" cy="6" r="5.5"/></svg></li>
      <li>Elmvale, Sorrin, Calderia
        <svg viewBox="0 0 12 12"><path d="M6 0a4 4 0 0 1 4 4c0 3-4 8-4 8S2 7 2 4a4 4 0 0 1 4-4z"/></svg></li>
    </ul>

    <p class="brand-name">MBH</p>

    <svg class="edge-band" viewBox="0 0 525 14" preserveAspectRatio="none" aria-hidden="true">
      <polygon points="0,0 340,0 330,14 0,14" fill="var(--brand-blue)"/>
      <polygon points="340,0 525,0 525,14 330,14" fill="var(--accent-yellow)"/>
    </svg>
  </section>

</main>
</body>
</html>
```